AMAZING BLACK FRIDAY AD FOR PRINT OR THE WEB

Create a Black Friday ad for nitrile gloves. We are offering a box of 100, no-powder, exam grade nitrile gloves, for $9.99. No limit. Each case is $99. Create something simple, eye catching, cool. KestrelWrap.com. Sale ends on December 4th. While supplies last. We are a local medical supply company in Hawaii that serves the general public in addition to local businesses, government, etc. Gloves are in short supply and we have tons of inventory ready to sell.

Target Market(s)

Businesses that use supplies such as gloves

Industry/Entity Type

medical supplies

Requirements
Must have
• logo and website

```html
<!DOCTYPE html>
<html lang="en">
<head>
<meta charset="UTF-8">
<title>Black Friday Sale – Nitrile Gloves – KestrelWrap.com</title>
<link rel="stylesheet" href="https://fonts.googleapis.com/css2?family=Bebas+Neue&family=Kaushan+Script&family=Montserrat:wght@400;600;700;800;900&display=swap">
<style>
  :root {
    --ink: #0b0b0b;
    --charcoal: #3c3c3c;
    --body-grey: #6f6f6f;
    --brand-green: #0a9044;
    --headline-green: #0a8a3e;
    --sale-red: #e8141b;
    --glove-blue: #4aa9e8;
    --glove-blue-light: #8fd0f7;
    --dot-grey: #eeeeee;
    --paper: #ffffff;
  }
  * { margin: 0; padding: 0; box-sizing: border-box; }
  html, body { width: 1200px; height: 1200px; overflow: hidden; background: var(--paper); }
  .ad {
    position: relative;
    width: 1200px; height: 1200px;
    background: var(--paper);
    font-family: "Montserrat", Arial, sans-serif;
    overflow: hidden;
  }
  .dot-field {
    position: absolute;
    background: var(--dot-grey);
    border-radius: 10px;
  }
  .dot-field--a { left: 694px; top: 83px; width: 40px; height: 106px; }
  .dot-field--b { left: 1017px; top: 80px; width: 107px; height: 37px; }
  .dot-field--c { left: 1064px; top: 176px; width: 60px; height: 35px; }
  .dot-field--d { left: 458px; top: 1017px; width: 109px; height: 36px; }
  .dot-field--e { left: 533px; top: 1078px; width: 109px; height: 39px; }

  .headline {
    position: absolute;
    left: 64px;
    font-family: "Bebas Neue", Impact, sans-serif;
    font-size: 268px;
    line-height: 1;
    color: var(--ink);
    letter-spacing: 0;
  }
  .headline--black { top: 44px; }
  .headline--friday { top: 244px; }

  .offer-card {
    position: absolute;
    left: 680px; top: 426px;
    width: 407px; height: 713px;
    background: var(--brand-green);
    border-radius: 4px 4px 46px 46px;
  }

  .glove-photo {
    position: absolute;
    left: 600px; top: 40px;
    width: 540px; height: 425px;
    background: radial-gradient(ellipse at 45% 45%, var(--glove-blue-light), var(--glove-blue) 70%);
    border-radius: 48% 52% 40% 60% / 55% 45% 55% 45%;
    transform: rotate(-6deg);
  }

  .sale-script {
    position: absolute;
    left: 130px; top: 392px;
    font-family: "Kaushan Script", cursive;
    font-size: 196px;
    line-height: 1.1;
    color: var(--sale-red);
    transform: rotate(-7deg);
  }

  .deadline-line {
    position: absolute;
    left: 94px;
    line-height: 1;
    text-transform: uppercase;
    white-space: nowrap;
  }
  .deadline-line--lead { top: 658px; font-weight: 800; font-size: 61px; color: var(--charcoal); }
  .deadline-line--date { top: 719px; font-weight: 800; font-size: 61px; color: var(--headline-green); }
  .deadline-line--date sup { font-size: 28px; vertical-align: 26px; margin-left: 2px; }
  .deadline-line--note { top: 785px; font-weight: 400; font-size: 30px; color: var(--charcoal); }
  .deadline-rule {
    position: absolute;
    left: 94px; top: 826px;
    width: 487px; height: 4px;
    background: var(--headline-green);
  }
  .about {
    position: absolute;
    left: 95px; top: 846px;
    font-weight: 600;
    font-size: 17px;
    line-height: 27.5px;
    color: var(--body-grey);
    white-space: nowrap;
  }

  .brand-name {
    position: absolute;
    left: 108px; top: 1076px;
    font-weight: 700;
    font-size: 36px;
    line-height: 1;
    color: var(--charcoal);
    letter-spacing: -0.5px;
    white-space: nowrap;
  }

  .card-content {
    position: absolute;
    left: 731px; top: 508px;
    width: 300px;
    color: var(--paper);
  }
  .card-title {
    font-weight: 900;
    font-size: 70px;
    line-height: 63px;
    color: var(--ink);
    letter-spacing: 0.5px;
  }
  .card-rule { height: 3px; background: var(--paper); }
  .card-rule--title { margin-top: 22px; }
  .card-pack {
    font-weight: 800;
    font-size: 27px;
    line-height: 30px;
    padding: 14px 0 13px;
    text-transform: uppercase;
  }
  .feature-list { list-style: none; padding: 18px 0 14px; }
  .feature {
    display: flex; align-items: center; gap: 19px;
    font-weight: 800; font-size: 24px; line-height: 26px;
    margin-bottom: 14px;
  }
  .feature:last-child { margin-bottom: 0; }
  .feature__icon { width: 50px; height: 50px; flex: none; }
  .price-row {
    display: flex; align-items: center; gap: 12px;
    padding: 16px 0 14px;
  }
  .price-row__amount {
    font-weight: 900; font-size: 74px; line-height: 1; letter-spacing: -1px;
  }
  .price-row__amount sup, .case-row__amount sup { font-size: 0.45em; vertical-align: 0.9em; }
  .price-row__limit {
    font-weight: 600; font-size: 25px; line-height: 26px; text-transform: uppercase;
  }
  .case-row {
    display: flex; align-items: center; gap: 20px;
    padding-top: 12px;
  }
  .case-row__label {
    font-weight: 900; font-size: 34px; line-height: 34px; text-transform: uppercase;
  }
  .case-row__amount {
    font-weight: 900; font-size: 86px; line-height: 1; letter-spacing: -1px;
  }
</style>
</head>
<body>
<main class="ad">
  <div class="dot-field dot-field--a" role="img" aria-label="Grey dot grid decoration"></div>
  <div class="dot-field dot-field--b" role="img" aria-label="Grey dot grid decoration"></div>
  <div class="dot-field dot-field--c" role="img" aria-label="Grey dot grid decoration"></div>
  <div class="dot-field dot-field--d" role="img" aria-label="Grey dot grid decoration"></div>
  <div class="dot-field dot-field--e" role="img" aria-label="Grey dot grid decoration"></div>

  <h1 class="headline headline--black">BLACK</h1>
  <div class="headline headline--friday">FRIDAY</div>

  <section class="offer-card"></section>
  <div class="glove-photo" role="img" aria-label="Photo of a pair of blue nitrile exam gloves"></div>

  <div class="sale-script">Sale</div>

  <div class="deadline-line deadline-line--lead">Sale ends on</div>
  <div class="deadline-line deadline-line--date">December 4<sup>TH</sup></div>
  <div class="deadline-line deadline-line--note">Till supplies last</div>
  <div class="deadline-rule"></div>
  <p class="about">We are a local medical supply company in Hawaii<br>that serves the general public in addition to local<br>businesses, government, etc. Gloves are in short<br>supply and we have tons of inventory ready to sell.</p>

  <div class="brand-name">kestrelwrap.com</div>

  <div class="card-content">
    <h2 class="card-title">NITRILE<br>GLOVES</h2>
    <div class="card-rule card-rule--title"></div>
    <p class="card-pack">We are offering<br>a box of 100</p>
    <div class="card-rule"></div>
    <ul class="feature-list">
      <li class="feature">
        <svg class="feature__icon" viewBox="0 0 50 50" aria-hidden="true">
          <circle cx="25" cy="25" r="22" fill="none" stroke="#fff" stroke-width="3"/>
          <rect x="18" y="16" width="14" height="18" rx="2" fill="none" stroke="#fff" stroke-width="2.5" transform="rotate(-35 25 25)"/>
          <line x1="12" y1="12" x2="38" y2="38" stroke="#fff" stroke-width="3"/>
        </svg>
        <span>No-powder</span>
      </li>
      <li class="feature">
        <svg class="feature__icon" viewBox="0 0 50 50" aria-hidden="true">
          <circle cx="25" cy="25" r="22" fill="none" stroke="#fff" stroke-width="3"/>
          <rect x="16" y="13" width="15" height="21" rx="2" fill="none" stroke="#fff" stroke-width="2.5"/>
          <line x1="19" y1="19" x2="28" y2="19" stroke="#fff" stroke-width="2"/>
          <line x1="19" y1="24" x2="26" y2="24" stroke="#fff" stroke-width="2"/>
          <circle cx="32" cy="33" r="6" fill="#0a9044" stroke="#fff" stroke-width="2.5"/>
          <polyline points="29.5,33 31.5,35 35,31" fill="none" stroke="#fff" stroke-width="2"/>
        </svg>
        <span>Exam grade<br>nitrile gloves</span>
      </li>
    </ul>
    <div class="card-rule"></div>
    <div class="price-row">
      <span class="price-row__amount"><sup>$</sup>9.99</span>
      <span class="price-row__limit">No<br>limit</span>
    </div>
    <div class="card-rule"></div>
    <div class="case-row">
      <span class="case-row__label">Each<br>case</span>
      <span class="case-row__amount"><sup>$</sup>99</span>
    </div>
  </div>
</main>
</body>
</html>
```